Ripple Over Tuesday (Podcast Artwork)

We require a podcast cover artwork, to stand out but also make our direction clear. This is a podcast about how everyone can make effective change to help the environment and limit the climate crisis.

The artwork needs to be 3000x3000 pixels for submission to Quillfern Podcasts.

We would ideally like a planet image in there, perhaps within one of the 'o's. However, we are open to suggestions and alternative design options.

The use of green in the artwork would also be good.

```html
<!DOCTYPE html>
<html lang="en">
<head>
<meta charset="utf-8">
<title>Ripple Over Tuesday — Podcast Cover</title>
<link rel="stylesheet" href="https://fonts.googleapis.com/css2?family=Montserrat:wght@700;800&display=swap">
<style>
  :root {
    --ink: #ffffff;
    --sun: #f0c800;
    --lime: #a6dc1a;
    --leaf: #3cc24a;
    --teal: #0aa8a8;
    --ocean: #0560c8;
    --deep: #0a1a94;
    --band-dark: rgba(20, 90, 60, 0.18);
    --band-light: rgba(255, 255, 255, 0.10);
  }
  * { margin: 0; padding: 0; box-sizing: border-box; }
  html, body {
    width: 1200px;
    height: 1200px;
    overflow: hidden;
  }
  .cover {
    position: relative;
    width: 1200px;
    height: 1200px;
    overflow: hidden;
    background: linear-gradient(45deg, var(--sun) 0%, var(--lime) 22%, var(--leaf) 45%, var(--teal) 65%, var(--ocean) 85%, var(--deep) 100%);
    font-family: "Montserrat", sans-serif;
    color: var(--ink);
  }
  .cover__waves {
    position: absolute;
    inset: 0;
    width: 100%;
    height: 100%;
  }
  .title {
    position: absolute;
    left: 0;
    top: 0;
    width: 100%;
    height: 100%;
  }
  .title__lead {
    position: absolute;
    left: 218px;
    top: 152px;
    font-weight: 800;
    font-size: 72px;
    line-height: 84px;
    letter-spacing: 0.32em;
    text-transform: uppercase;
  }
  .title__lead span { display: block; }
  .title__main {
    position: absolute;
    left: 0;
    width: 100%;
    top: 470px;
    text-align: center;
    font-weight: 800;
    font-size: 158px;
    line-height: 1;
    letter-spacing: 0.01em;
    text-transform: uppercase;
    text-shadow: 0 2px 6px rgba(0, 60, 40, 0.18);
  }
  .format-label {
    position: absolute;
    left: 221px;
    top: 838px;
    display: grid;
    grid-template-columns: repeat(3, 86px);
    row-gap: 38px;
    font-weight: 700;
    font-size: 42px;
    line-height: 44px;
    text-transform: uppercase;
  }
</style>
</head>
<body>
  <main class="cover">
    <svg class="cover__waves" viewBox="0 0 1200 1200" aria-hidden="true">
      <path d="M0 660 C 380 470, 760 260, 1040 0 L 1200 0 L 1200 0 C 900 280, 500 520, 0 770 Z" fill="var(--band-dark)"/>
      <path d="M0 950 C 360 1080, 760 1000, 1200 319 L 1200 1200 L 0 1200 Z" fill="var(--band-light)"/>
      <path d="M0 770 C 420 560, 860 340, 1200 319 L 1200 1200 L 0 1200 Z" fill="rgba(255,255,255,0.06)"/>
    </svg>

    <h1 class="title">
      <span class="title__lead"><span>Ripple</span><span>Over</span></span>
      <span class="title__main">Tuesday</span>
    </h1>

    <p class="format-label" aria-label="Podcast">
      <span>P</span><span>O</span><span>D</span>
      <span>C</span><span>A</span><span>S</span>
      <span>T</span>
    </p>
  </main>
</body>
</html>
```